Uprising SaaS company needs an attractive business card design

We're an uprising SaaS company who's attempting to attack the rigid car (insurance) claims management market in Europe.
We want to our mighty base order management system, listen to our clients to connect the smart ideas to build something even mightier.
We primarily focus on helping our customers manage their customers' claims/orders and get them resolved as smoothly as possible.
We'd like the business card design to express technical innovation and the fact that we connect smart ideas, as our company slogan indicates.
Contact Information for Business Card
Name, position, website, email, mobile, business address
Font styles to use
Colors
Designer to choose colors to be used in the design.
Look and feel
Each slider illustrates characteristics of the customer's brand and the style your logo design should communicate.

```html
<!DOCTYPE html>
<html lang="en">
<head>
<meta charset="utf-8">
<title>Nexovia Business Card</title>
<link href="https://fonts.googleapis.com/css2?family=Montserrat:wght@700&family=Quicksand:wght@400;500&display=swap" rel="stylesheet">
<style>
  :root {
    --sky: #7ecfe5;
    --sky-soft: #8fd6ea;
    --ice: #eef7fc;
    --white: #ffffff;
    --ink: #6c6f73;
    --logo-grey: #7b8287;
    --stage: #2b2b2b;
  }
  * { box-sizing: border-box; margin: 0; padding: 0; }
  html, body { width: 1200px; height: 1200px; overflow: hidden; }
  body {
    background: var(--stage);
    display: flex; flex-direction: column; align-items: center; justify-content: center;
    gap: 60px;
    font-family: "Quicksand", sans-serif;
  }
  .card {
    position: relative; width: 760px; height: 492px;
    border-radius: 34px; overflow: hidden;
    box-shadow: 0 18px 40px rgba(0,0,0,.45);
  }

  /* Front */
  .card-front { background: var(--sky); }
  .front-band-tagline { position: absolute; left: 0; right: 0; top: 54%; height: 24%; background: var(--white);
    display: flex; align-items: center; justify-content: center; }
  .front-band-gap { position: absolute; left: 0; right: 0; top: 88%; height: 6%; background: var(--white); }
  .tagline { font-family: "Montserrat", sans-serif; font-weight: 700; font-size: 34px; letter-spacing: 2px; color: var(--sky); }
  .front-wordmark { position: absolute; left: 0; right: 0; top: 16%; text-align: center;
    font-family: "Quicksand", sans-serif; font-weight: 400; font-size: 116px; color: var(--white); letter-spacing: 2px; line-height: 1; }
  .facet { position: absolute; background: rgba(255,255,255,.08); }
  .facet-a { left: 60px; top: -40px; width: 260px; height: 420px; transform: skewX(-18deg); }

  /* Back */
  .card-back { background: linear-gradient(90deg, var(--white) 0%, var(--white) 55%, var(--ice) 55%); }
  .back-band { position: absolute; left: 0; right: 0; top: 67%; height: 22%; background: var(--sky);
    display: flex; align-items: center; justify-content: space-between; padding: 0 44px; }
  .company { font-family: "Montserrat", sans-serif; font-weight: 700; font-size: 34px; color: var(--white); letter-spacing: 1px; }
  .address { font-family: "Montserrat", sans-serif; font-weight: 700; font-size: 17px; color: var(--white); text-align: right; line-height: 1.5; }
  .back-wordmark { position: absolute; left: 56px; top: 30%; display: flex; align-items: center; gap: 14px;
    font-weight: 500; font-size: 78px; color: var(--logo-grey); line-height: 1; }
  .wordmark-dot { width: 16px; height: 16px; border-radius: 50%; background: var(--sky); }
  .person { position: absolute; right: 44px; top: 40px; width: 320px; }
  .person-name { font-size: 40px; font-weight: 500; color: var(--sky); line-height: 1.1; border-bottom: 1.5px solid var(--ink); padding-bottom: 6px; }
  .person-role { font-family: "Montserrat", sans-serif; font-weight: 700; font-size: 15px; color: var(--ink); letter-spacing: 1px; padding: 6px 0 8px; border-bottom: 1.5px solid var(--ink); width: 60%; }
  .contact-list { list-style: none; margin-top: 16px; }
  .contact-list li { display: flex; align-items: center; gap: 14px; font-size: 18px; color: var(--ink); margin-bottom: 8px; }
  .contact-list svg { width: 18px; height: 18px; fill: var(--sky); flex: none; }
</style>
</head>
<body>

<section class="card card-front" aria-label="Business card front">
  <div class="facet facet-a"></div>
  <div class="front-wordmark">nexovia</div>
  <div class="front-band-tagline"><p class="tagline">Building Clever Links</p></div>
  <div class="front-band-gap"></div>
</section>

<section class="card card-back" aria-label="Business card back">
  <div class="back-wordmark"><span class="wordmark-dot"></span>nexovia</div>
  <div class="person">
    <p class="person-name">Lukas Brenner</p>
    <p class="person-role">CEO</p>
    <ul class="contact-list">
      <li><svg viewBox="0 0 24 24"><path d="M6.6 10.8a15 15 0 0 0 6.6 6.6l2.2-2.2a1 1 0 0 1 1-.25 11.4 11.4 0 0 0 3.6.57 1 1 0 0 1 1 1V20a1 1 0 0 1-1 1A17 17 0 0 1 3 4a1 1 0 0 1 1-1h3.5a1 1 0 0 1 1 1c0 1.25.2 2.45.57 3.57a1 1 0 0 1-.25 1z"/></svg>+49 170 5550142</li>
      <li><svg viewBox="0 0 24 24"><path d="M2 5h20v14H2z M2 5l10 8 10-8" fill="var(--sky)" stroke="var(--white)" stroke-width="1.5"/></svg>info@nexovia.com</li>
      <li><svg viewBox="0 0 24 24"><circle cx="12" cy="12" r="10"/><path d="M2 12h20M12 2c3 3 3 17 0 20M12 2c-3 3-3 17 0 20" stroke="var(--white)" stroke-width="1.5" fill="none"/></svg>www.nexovia.com</li>
    </ul>
  </div>
  <div class="back-band">
    <p class="company">Nexovia GmbH</p>
    <p class="address">Lindenweg 14b<br>10115 Berlin, Germany</p>
  </div>
</section>

</body>
</html>
```